Business Advisory Firm Business Card

A clean, very upscale looking business card. Not crowded.

Please include logo (attached) and:

Daria K. Pellworth
Four Marlow Court
New York, NY 10023
tel: (917) 555-0143
fax: (646) 555-0172
email: dpellworth@quarrystoneconsultants.example
website: www.quarrystoneconsultants.example

Target Market(s)

Business clients. Often real estate development firms, other advisory firms or growing companies that need assistance. I would like a card that looks impressive and confident.

Industry/Entity Type

Business

Colors

Designer to choose colors to be used in the design.

Requirements
Must have
• Impressive and confident. Please include logo.
Should not have
• nothing flashy...

```html
<!DOCTYPE html>
<html lang="en">
<head>
<meta charset="UTF-8">
<title>Quarrystone Advisory Services — Business Card</title>
<link rel="stylesheet" href="https://fonts.googleapis.com/css2?family=Questrial&display=swap">
<style>
  :root {
    --paper: #ffffff;
    --ink: #2b2b2b;
    --ink-soft: #5a5a5a;
    --brand-green: #a5cf4c;
    --mark-grey: #8a8c8e;
    --name-white: #ffffff;
  }
  html, body {
    margin: 0;
    padding: 0;
    overflow: hidden;
    background: var(--paper);
  }
  .card {
    position: relative;
    width: 1200px;
    height: 668px;
    background: var(--paper);
    overflow: hidden;
    font-family: "Questrial", sans-serif;
  }
  .brand-mark {
    position: absolute;
    left: 72px;
    top: 70px;
    width: 180px;
    height: 180px;
    background: var(--mark-grey);
  }
  .brand-name {
    position: absolute;
    left: 305px;
    top: 88px;
    margin: 0;
    font-weight: 400;
    font-size: 50px;
    line-height: 54px;
    color: var(--ink);
    font-variant: small-caps;
    letter-spacing: 1px;
  }
  .name-panel {
    position: absolute;
    left: 714px;
    top: 90px;
    width: 486px;
    height: 289px;
    background: var(--brand-green);
  }
  .person-name {
    position: absolute;
    right: 24px;
    bottom: 14px;
    margin: 0;
    font-size: 26px;
    letter-spacing: 4px;
    color: var(--name-white);
    text-transform: uppercase;
  }
  .contact {
    position: absolute;
    right: 14px;
    top: 458px;
    margin: 0;
    font-style: normal;
    text-align: right;
    font-size: 29px;
    line-height: 40.5px;
    letter-spacing: 2.2px;
    color: var(--ink-soft);
  }
  .contact span { display: block; }
</style>
</head>
<body>
  <div class="card">
    <div class="brand-mark" aria-hidden="true"></div>
    <h1 class="brand-name">Quarrystone<br>Advisory<br>Services, Inc.</h1>

    <div class="name-panel">
      <p class="person-name">Daria K. Pellworth</p>
    </div>

    <address class="contact">
      <span class="contact-street">Four Marlow Court, New York, NY 10023</span>
      <span class="contact-phones">t: (917) 555-0143 | f: (646) 555-0172</span>
      <span class="contact-email">e: dpellworth@quarrystoneconsultants.example</span>
      <span class="contact-web">W: www.quarrystoneconsultants.example</span>
    </address>
  </div>
</body>
</html>
```